Admin Backend Redesign

We need a redesign for our backend which supoosed to make the backoffice look more modern!

I will add screenshots of the backoffice so you know what data will be shown in the Admin.

Have in mind that the users of this backend are Doctors. We need a clinical look, modern and sharp. The backoffice is responsive, have that in mind. We need the backoffice to look as professional as possible.

The theme used for the website is: http://velmora.quillstack-sample.com/

ON the main page of the backoffice, under every widget i need some space to write an explanation what the widget is about.

The color code used in our logo and website is #57aad4 combined with white.

We are open for ideas!
Updates

Project Deadline Extended
Reason: Designs are ok, but nothing innovative. Please use more modern designs!

Project Deadline Extended
Reason: Havent recieved a perfect design yet. Please read instructions carefully! Thank you

Project Deadline Extended
Reason: Hey everybody, sorry for the delay. We will decide in 3 days. If anyone wants to add a Design, that would be great.

Target Market(s)

Doctors, therapists

Industry/Entity Type

It Professional

Font styles to use
Sans Serif

Requirements
Must have
• Must look uptodate, modern, like new back offices look nowadays

```html
<!DOCTYPE html>
<html lang="de">
<head>
<meta charset="utf-8">
<title>Admin Backend – Arzt Verwalten</title>
<link href="https://fonts.googleapis.com/css2?family=Open+Sans:wght@400;600;700&family=Arimo:wght@400&display=swap" rel="stylesheet">
<style>
:root{
  --side:#272c30;
  --side-dark:#1f2326;
  --topbar:#eef0f1;
  --page:#d9dcdf;
  --card:#ffffff;
  --card-head:#6b6b6b;
  --accent:#57aad4;
  --green:#8cc63f;
  --red:#e04a52;
  --icon:#7b8793;
  --label:#333333;
  --field-border:#dcdcdc;
}
*{box-sizing:border-box;margin:0;padding:0}
html,body{width:1200px;height:1200px;overflow:hidden}
body{position:relative;background:var(--page);font-family:"Open Sans",sans-serif}
.sidebar{position:absolute;left:0;top:0;width:263px;height:1132px;background:var(--side)}
.brand{height:100px;background:var(--side-dark);display:flex;align-items:center;justify-content:center;color:var(--accent);font-size:25px;letter-spacing:.5px}
.profile{position:absolute;top:140px;left:29px;width:234px;height:74px}
.avatar{position:absolute;border-radius:50%;background:radial-gradient(circle at 50% 40%,#c9a07f,#6e5443 70%,#3b2f29);border:3px solid #fff}
.profile .avatar{left:0;top:0;width:74px;height:74px}
.profile .info{position:absolute;left:84px;width:110px;top:8px;text-align:center;color:#fff;line-height:21px}
.info b{font-size:16px;font-weight:700;display:block}
.info .name{font-size:16px;display:block}
.info .status{font-size:13px}
.info .status span{color:var(--red)}
.nav{position:absolute;top:257px;left:0;width:263px;list-style:none}
.nav li{position:relative;height:51px;display:flex;align-items:center;padding-left:94px;color:#e8eaec;font-size:17px;letter-spacing:.5px}
.nav li svg{position:absolute;left:46px;top:15px}
.nav li.current{background:var(--side-dark)}
.nav li.marked::after{content:"";position:absolute;right:0;top:4px;width:6px;height:51px;background:var(--accent)}
.topbar{position:absolute;left:263px;top:0;width:937px;height:65px;background:var(--topbar)}
.topbar svg{position:absolute}
.search{position:absolute;left:168px;top:17px;width:221px;height:31px;background:#dadde0;border-radius:2px;color:#8a949e;font-size:16px;padding:4px 12px}
.badge{position:absolute;width:16px;height:16px;border-radius:50%;background:var(--red);color:#fff;font-size:10px;text-align:center;line-height:16px}
.user{position:absolute;left:703px;top:21px;color:var(--icon);font-size:19px}
.topbar .avatar{left:812px;top:12px;width:42px;height:42px;border-width:2px}
.card{position:absolute;left:310px;top:112px;width:831px;height:472px;background:var(--card);border-radius:8px;overflow:hidden}
.card h1{height:36px;background:var(--card-head);color:#fff;font-size:16px;font-weight:400;padding:7px 22px}
.row{position:absolute;display:flex;align-items:center;height:28px;font-family:Arimo,sans-serif;font-size:12px;color:var(--label)}
.row label{text-align:right;padding-right:16px}
.row label i{color:var(--red);font-style:normal;margin-left:5px}
.field{height:28px;border:1px solid var(--field-border);border-radius:2px;padding:6px 6px;color:#111;font-size:12px;position:relative}
.field.select::after{content:"▴\A▾";white-space:pre;position:absolute;right:5px;top:4px;font-size:7px;line-height:7px;color:#333}
.l label{width:134px}.l .field{width:233px}
.r label{width:536px;position:absolute;left:-536px}.r{left:537px}.r .field{width:233px}
.toggle{width:33px;height:12px;background:#111;border-radius:2px;display:flex;align-items:center;gap:2px;padding:0 2px}
.toggle span{width:8px;height:8px;border-radius:50%;background:#777}
.toggle span.on{background:#3cdc3c}
.btn{position:absolute;top:421px;height:31px;color:#fff;font-size:13px;text-align:center;line-height:31px;font-family:Arimo,sans-serif}
.btn.save{left:21px;width:119px;background:var(--green)}
.btn.cancel{left:152px;width:88px;background:var(--accent)}
.footer{position:absolute;left:0;top:1132px;width:1200px;height:68px;background:var(--side);color:#fff;font-family:Arimo,sans-serif;font-size:12px;text-align:center;line-height:68px}
</style>
</head>
<body>
<aside class="sidebar">
  <div class="brand">Admin Backend</div>
  <div class="profile">
    <div class="avatar" role="img" aria-label="Profilfoto des Benutzers"></div>
    <div class="info"><b>Welcome</b><span class="name">Dr.Adrian</span><span class="status">Status: <span>Online</span></span></div>
  </div>
  <ul class="nav">
    <li class="current"><svg width="22" height="22" viewBox="0 0 22 22" fill="none" stroke="#e8eaec" stroke-width="1.8"><circle cx="11" cy="11" r="9"/><path d="M11 11l3-5"/></svg>Dashboard</li>
    <li class="marked"><svg width="22" height="22" viewBox="0 0 22 22" fill="none" stroke="#aab2ba" stroke-width="1.3"><circle cx="11" cy="11" r="3"/><path d="M9.5 2h3l.5 2.5 2 1 2.3-1.2 2 2-1.2 2.3 1 2L21 11v0l-2.5.5-1 2 1.2 2.3-2 2-2.3-1.2-2 1L12.5 20h-3l-.5-2.5-2-1-2.3 1.2-2-2 1.2-2.3-1-2L1 11l2.5-.5 1-2-1.2-2.3 2-2 2.3 1.2 2-1z"/></svg>Mein Konto</li>
    <li><svg width="22" height="22" viewBox="0 0 22 22" fill="none" stroke="#aab2ba" stroke-width="1.3"><circle cx="11" cy="11" r="3"/><path d="M9.5 2h3l.5 2.5 2 1 2.3-1.2 2 2-1.2 2.3 1 2L21 11v0l-2.5.5-1 2 1.2 2.3-2 2-2.3-1.2-2 1L12.5 20h-3l-.5-2.5-2-1-2.3 1.2-2-2 1.2-2.3-1-2L1 11l2.5-.5 1-2-1.2-2.3 2-2 2.3 1.2 2-1z"/></svg>Pateinten</li>
  </ul>
</aside>

<header class="topbar">
  <svg style="left:29px;top:24px" width="20" height="18" fill="var(--icon)"><rect width="20" height="3"/><rect y="7" width="20" height="3"/><rect y="14" width="20" height="3"/></svg>
  <svg style="left:68px;top:23px" width="20" height="20" viewBox="0 0 20 20" fill="none" stroke="var(--icon)" stroke-width="3"><path d="M3 10a7 7 0 0 1 12-5"/><path d="M17 10a7 7 0 0 1-12 5"/><path d="M15 1v5h-5M5 19v-5h5" stroke-width="2.5"/></svg>
  <svg style="left:109px;top:23px" width="21" height="21" fill="var(--icon)"><rect width="9" height="9"/><rect x="12" width="9" height="9"/><rect y="12" width="9" height="9"/><rect x="12" y="12" width="9" height="9"/></svg>
  <div class="search">Search</div>
  <svg style="left:360px;top:24px" width="18" height="18" fill="none" stroke="var(--icon)" stroke-width="2"><circle cx="7" cy="7" r="5.5"/><path d="M11 11l5 5"/></svg>
  <svg style="left:639px;top:25px" width="28" height="19" fill="var(--icon)"><rect width="28" height="19" rx="1"/><path d="M1 1l13 10L27 1" stroke="#eef0f1" stroke-width="2" fill="none"/></svg>
  <div class="badge" style="left:634px;top:19px">7</div>
  <div class="badge" style="left:692px;top:19px">3</div>
  <div class="user">Dr.Adrian <svg style="position:static" width="10" height="7" fill="none" stroke="var(--icon)" stroke-width="2"><path d="M1 1l4 4 4-4"/></svg></div>
  <div class="avatar" role="img" aria-label="Profilfoto des Benutzers"></div>
  <svg style="left:874px;top:21px" width="26" height="26" viewBox="0 0 22 22" fill="var(--icon)"><path d="M9.5 1h3l.6 2.7 2 .9 2.4-1.5 2.1 2.1-1.5 2.4.9 2 2.7.6v3l-2.7.6-.9 2 1.5 2.4-2.1 2.1-2.4-1.5-2 .9-.6 2.7h-3l-.6-2.7-2-.9-2.4 1.5-2.1-2.1 1.5-2.4-.9-2L1 12.5v-3l2.7-.6.9-2-1.5-2.4 2.1-2.1 2.4 1.5 2-.9z"/><circle cx="11" cy="11" r="3.3" fill="#eef0f1"/></svg>
</header>

<main class="card">
  <h1>Arzt Verwalten</h1>
  <div class="row l" style="top:53px"><label>Benutzer Rechte<i>*</i></label><div class="field select">Doctor</div></div>
  <div class="row r" style="top:53px"><label>Vorname<i>*</i></label><div class="field">Dr.</div></div>
  <div class="row l" style="top:98px"><label>Nachname<i>*</i></label><div class="field">Lindqvist</div></div>
  <div class="row r" style="top:98px"><label>E-Mail<i>*</i></label><div class="field">demo4@example.de</div></div>
  <div class="row l" style="top:142px"><label>Tel<i>*</i></label><div class="field">0221 555014700</div></div>
  <div class="row r" style="top:142px"><label>Praxisname</label><div class="field">Clarion Praxis</div></div>
  <div class="row l" style="top:187px"><label>Strasse<i>*</i></label><div class="field">Lindenweg 12</div></div>
  <div class="row r" style="top:187px"><label>Postleitzahl</label><div class="field">50321</div></div>
  <div class="row l" style="top:231px"><label>Ort<i>*</i></label><div class="field">Kelldorf</div></div>
  <div class="row r" style="top:231px"><label>Deutschland<i>*</i></label><div class="field select">Germany</div></div>
  <div class="row l" style="top:276px"><label>Paket<i>*</i></label><div class="field">12 Monate</div></div>
  <div class="row r" style="top:276px"><label>Zahlungsart<i>*</i></label><div class="field">MANUAL</div></div>
  <div class="row l" style="top:320px"><label>Mitglied seit</label><div class="field">2014-06-03 12:12:05</div></div>
  <div class="row r" style="top:320px"><label>Ablauf der Mitgliedschaft</label><div class="field">2015-06-03 12:12</div></div>
  <div class="row l" style="top:365px"><label>Website</label></div>
  <div class="row r" style="top:358px"><label>Öffentlicher Status</label><div class="toggle"><span></span><span></span><span class="on"></span></div></div>
  <div class="btn save">Aktualisieren</div>
  <div class="btn cancel">Storno</div>
</main>

<footer class="footer">© 2014 - Admin Backend All Rights Reserved.</footer>
</body>
</html>
```